Whitmore Business Card Design

The name of the business is Dara Whitmore, CPA LLC
The service that we offer is Accounting, Tax & Consulting Services. I need it to have the following items:
Dara Whitmore, Principal
Phone Number
Email Address
Physical Address

I have attached the company logo, one in black and one in white. Please provide a design in black background and the other in white background. Please include "Accounting, Tax & Consulting Services". I want the business card to be clean and very professional.

```html
<!DOCTYPE html>
<html lang="en">
<head>
<meta charset="utf-8">
<title>Dara Whitmore, CPA LLC – Business Card</title>
<link href="https://fonts.googleapis.com/css2?family=Lato:wght@400;700&display=swap" rel="stylesheet">
<style>
  :root {
    --canvas: #e9e7e4;
    --card-dark: #353638;
    --block-dark: #3f4042;
    --card-light: #ffffff;
    --block-light: #eeeeee;
    --ink-dark: #3a3b3d;
    --brand-red: #9e1c22;
    --muted: #7a7b7d;
    --rule: #b9babb;
    --on-dark: #ffffff;
    --on-dark-muted: #9a9b9d;
  }
  * { box-sizing: border-box; margin: 0; padding: 0; }
  html, body {
    width: 1200px; height: 900px; overflow: hidden;
    background: var(--canvas);
    font-family: "Lato", Arial, sans-serif;
  }
  .stage { position: relative; width: 1200px; height: 900px; }

  .card {
    position: absolute;
    width: 630px; height: 360px;
    left: 285px;
    overflow: hidden;
    box-shadow: 0 10px 28px rgba(0,0,0,.22);
  }
  .card--front { top: 50px; background: var(--card-dark); }
  .card--back {
    top: 470px;
    background: linear-gradient(200deg, var(--card-light) 40%, #f1f1f1 100%);
  }

  /* Geometric background blocks */
  .block { position: absolute; }
  .card--front .block { background: var(--block-dark); }
  .card--back .block { background: var(--block-light); }
  .block--a { left: 20px;  top: 36px;  width: 300px; height: 32px; }
  .block--b { left: 40px;  top: 68px;  width: 32px;  height: 110px; }
  .block--c { left: 190px; top: 150px; width: 150px; height: 32px; }
  .block--d { left: 340px; top: 150px; width: 34px;  height: 210px; }
  .block--e { left: 0;     top: 205px; width: 190px; height: 32px; }
  .block--f { left: 40px;  top: 268px; width: 210px; height: 32px; }
  .block--g { left: 250px; top: 312px; width: 200px; height: 32px; }

  .card--back .block--a { left: 0;     top: 120px; width: 290px; height: 30px; }
  .card--back .block--b { left: 40px;  top: 150px; width: 30px;  height: 120px; }
  .card--back .block--c { left: 260px; top: 170px; width: 150px; height: 30px; }
  .card--back .block--d { left: 410px; top: 170px; width: 32px;  height: 190px; }
  .card--back .block--e { left: 90px;  top: 232px; width: 170px; height: 30px; }
  .card--back .block--f { left: 0;     top: 290px; width: 230px; height: 30px; }
  .card--back .block--g { display: none; }

  .wordmark {
    position: absolute;
    right: 60px;
    text-align: right;
    z-index: 1;
  }
  .card--front .wordmark { top: 120px; }
  .card--back .wordmark { top: 44px; right: 56px; }
  .wordmark__square {
    display: inline-block;
    width: 16px; height: 16px;
    margin-right: 12px;
    vertical-align: 2px;
    background: var(--brand-red);
  }
  .wordmark__name {
    font-weight: 700;
    font-size: 30px;
    letter-spacing: .02em;
    text-transform: uppercase;
  }
  .wordmark__tagline {
    margin-top: 8px;
    font-size: 14px;
    letter-spacing: .22em;
    text-transform: uppercase;
  }
  .wordmark__services {
    margin-top: 14px;
    font-size: 13px;
    letter-spacing: .06em;
  }
  .card--front .wordmark__name { color: var(--on-dark); }
  .card--front .wordmark__tagline { color: var(--on-dark-muted); }
  .card--front .wordmark__services { color: var(--on-dark); }
  .card--back .wordmark__name { color: var(--ink-dark); }
  .card--back .wordmark__tagline { color: var(--muted); }

  .person {
    position: absolute;
    left: 48px; top: 150px;
    z-index: 1;
  }
  .person__name {
    font-weight: 700; font-size: 26px;
    color: var(--brand-red);
    text-transform: uppercase;
    letter-spacing: .01em;
  }
  .person__role { font-size: 17px; color: var(--muted); margin-top: 2px; }

  .contact {
    position: absolute;
    left: 48px; right: 40px; bottom: 28px;
    list-style: none;
    font-size: 17px; color: var(--ink-dark);
    z-index: 1;
  }
  .contact__item { display: flex; align-items: center; gap: 12px; padding: 5px 0; }
  .contact__item svg { width: 18px; height: 18px; flex: none; fill: var(--brand-red); }
  .contact__item--address {
    border-top: 1px solid var(--rule);
    margin-top: 8px; padding-top: 10px;
  }
  .contact__rule {
    position: absolute;
    right: 0; top: -6px;
    width: 260px; height: 1px; background: var(--rule);
  }
</style>
</head>
<body>
<main class="stage">

  <section class="card card--front" aria-label="Business card, front">
    <div class="block block--a"></div>
    <div class="block block--b"></div>
    <div class="block block--c"></div>
    <div class="block block--d"></div>
    <div class="block block--e"></div>
    <div class="block block--f"></div>
    <div class="block block--g"></div>
    <div class="wordmark">
      <p class="wordmark__name"><span class="wordmark__square"></span>Dara Whitmore, CPA LLC</p>
      <p class="wordmark__tagline">Certified Public Accountant</p>
      <p class="wordmark__services">Accounting, Tax &amp; Consulting Services</p>
    </div>
  </section>

  <section class="card card--back" aria-label="Business card, back">
    <div class="block block--a"></div>
    <div class="block block--b"></div>
    <div class="block block--c"></div>
    <div class="block block--d"></div>
    <div class="block block--e"></div>
    <div class="block block--f"></div>
    <div class="block block--g"></div>
    <div class="wordmark">
      <p class="wordmark__name"><span class="wordmark__square"></span>Dara Whitmore, CPA LLC</p>
      <p class="wordmark__tagline">Certified Public Accountant</p>
    </div>

    <div class="person">
      <h1 class="person__name">Dara Whitmore</h1>
      <p class="person__role">Principal</p>
    </div>

    <ul class="contact">
      <li class="contact__item">
        <svg viewBox="0 0 24 24" aria-hidden="true"><path d="M6.6 10.8a15.1 15.1 0 0 0 6.6 6.6l2.2-2.2c.3-.3.7-.4 1-.2 1.1.4 2.3.6 3.6.6.6 0 1 .4 1 1V20c0 .6-.4 1-1 1A17 17 0 0 1 3 4c0-.6.4-1 1-1h3.5c.6 0 1 .4 1 1 0 1.3.2 2.5.6 3.6.1.3 0 .7-.2 1z"/></svg>
        <span>(00) 0000 0000</span>
      </li>
      <li class="contact__item">
        <svg viewBox="0 0 24 24" aria-hidden="true"><path d="M3 5h18v14H3zm2 2v.5l7 4.5 7-4.5V7zm0 2.8V17h14V9.8l-7 4.5z"/></svg>
        <span>dara@darawhitmorecpa.com</span>
      </li>
      <li class="contact__item contact__item--address">
        <svg viewBox="0 0 24 24" aria-hidden="true"><path d="M12 2a7 7 0 0 0-7 7c0 5 7 13 7 13s7-8 7-13a7 7 0 0 0-7-7zm0 9.5A2.5 2.5 0 1 1 12 6.5a2.5 2.5 0 0 1 0 5z"/></svg>
        <span>11 dummy city, dummy place, P.O Box 0000 Dummy Land</span>
      </li>
      <li class="contact__rule" aria-hidden="true"></li>
    </ul>
  </section>

</main>
</body>
</html>
```